Property development business card design

New build residential property developers. I want a professional look but customer friendly so not too corporate. I'm not sure what logo will look best so open to designs with either. Thank you

Also i don't want both names on one card its 2 names for 2 different cards but with the same design.

Industry/Entity Type

Residential

Contact Information for Business Card

ORV Developments Ltd,
58 Fenwick Lane,
Ipswich,
Suffolk,
IP7 2TW

Property Research Manager
Joanna Pembrett

Managing Director
Derek Lockwell

```html
<!DOCTYPE html>
<html lang="en">
<head>
<meta charset="utf-8">
<title>ORV Developments – Business Cards</title>
<link href="https://fonts.googleapis.com/css2?family=Ubuntu:wght@400;500;700&display=swap" rel="stylesheet">
<style>
  :root {
    --bg: #e4e6e8;
    --white: #ffffff;
    --brand-blue: #1f7fcc;
    --brand-blue-light: #3a97dc;
    --brand-green: #a6c83a;
    --ink-grey: #6d6f72;
    --ink-dark: #202326;
    --photo-sky: #9cc3e6;
    --photo-house: #e9ecee;
    --photo-grass: #6f9a3c;
    --photo-desk-light: #e7e9ec;
    --photo-desk-dark: #2a2c30;
  }
  * { box-sizing: border-box; margin: 0; padding: 0; }
  html, body {
    width: 1200px; height: 1000px; overflow: hidden;
    background: var(--bg);
    font-family: "Ubuntu", sans-serif;
  }
  .card {
    position: absolute;
    width: 660px; height: 390px;
    overflow: hidden;
    box-shadow: 0 10px 30px rgba(0,0,0,0.18);
  }

  /* Front */
  .card--front { left: 110px; top: 80px; background: var(--white); }
  .front-photo {
    position: absolute; inset: 0;
    clip-path: polygon(0 0, 46% 0, 36% 100%, 0 100%);
    background: linear-gradient(180deg, var(--photo-sky) 0%, var(--photo-house) 35%, var(--photo-house) 62%, var(--photo-grass) 100%);
  }
  .front-brand {
    position: absolute; left: 330px; top: 120px;
    display: flex; align-items: center; gap: 14px;
  }
  .brand-dot {
    width: 34px; height: 34px; border-radius: 50%;
    background: var(--brand-blue);
  }
  .brand-name {
    font-weight: 700; font-size: 44px; color: var(--brand-blue);
    letter-spacing: 1px;
  }
  .front-tagline {
    position: absolute; left: 420px; top: 68px;
    font-weight: 700; font-size: 24px; color: var(--ink-grey);
    letter-spacing: 0.5px;
  }
  .front-web {
    position: absolute; right: 36px; bottom: 70px;
    font-size: 19px; color: var(--ink-grey);
  }

  /* Back */
  .card--back { left: 430px; top: 530px; background: var(--photo-desk-dark); }
  .back-photo {
    position: absolute; left: 0; top: 0; width: 100%; height: 100px;
    background: linear-gradient(100deg, var(--photo-desk-dark) 0%, #6a6d72 35%, var(--photo-desk-light) 70%, #f5f6f7 100%);
  }
  .band { position: absolute; left: 0; width: 100%; }
  .band--blue {
    top: 100px; height: 128px;
    background: linear-gradient(180deg, var(--brand-blue-light), var(--brand-blue));
  }
  .band--green { top: 228px; height: 90px; background: var(--brand-green); }
  .back-photo-foot {
    position: absolute; left: 0; top: 318px; width: 100%; height: 72px;
    background: linear-gradient(90deg, #1c1e21, #3a3d42);
  }
  .back-badge {
    position: absolute; left: 40px; top: 110px;
    width: 190px; height: 190px; border-radius: 50%;
    background: var(--white);
    display: flex; align-items: center; justify-content: center;
    box-shadow: 0 3px 10px rgba(0,0,0,0.25);
  }
  .back-badge .brand-name { font-size: 52px; }
  .contact {
    position: absolute; left: 270px; color: var(--white);
  }
  .contact--person { top: 118px; }
  .person-name { font-weight: 700; font-size: 25px; }
  .person-role { font-size: 16px; margin-top: 2px; opacity: 0.95; }
  .person-lines { margin-top: 14px; font-size: 17px; line-height: 1.3; }
  .contact--company { top: 244px; }
  .company-name { font-weight: 700; font-size: 19px; }
  .company-address { font-size: 17px; margin-top: 4px; }
</style>
</head>
<body>
  <section class="card card--front" aria-label="Business card front">
    <div class="front-photo" role="img" aria-label="Photo of a family outside a white new-build house on a sunny day"></div>
    <div class="front-tagline">DEVELOPMENTS</div>
    <div class="front-brand">
      <span class="brand-dot"></span>
      <span class="brand-name">ORV</span>
    </div>
    <div class="front-web">www.orvdevelopments.com</div>
  </section>

  <section class="card card--back" aria-label="Business card back">
    <div class="back-photo" role="img" aria-label="Photo of hands signing documents at a desk"></div>
    <div class="band band--blue"></div>
    <div class="band band--green"></div>
    <div class="back-photo-foot" role="img" aria-label="Continuation of desk photo"></div>
    <div class="back-badge"><span class="brand-name">ORV</span></div>
    <div class="contact contact--person">
      <div class="person-name">Derek Lockwell</div>
      <div class="person-role">Managing Director</div>
      <div class="person-lines">
        <div>074 512 66 308</div>
        <div>derek@orvdev.co.uk</div>
      </div>
    </div>
    <div class="contact contact--company">
      <div class="company-name">ORV Developments Ltd</div>
      <div class="company-address">58 Fenwick Lane, Ipswich, Suffolk, IP7 2TW</div>
    </div>
  </section>
</body>
</html>
```